I have a logo and need to design the business card and stationery.

The uploaded logo image named as FERNHOLT CONTRACTS which is to be replaced to FERNHOLT CONTRACTS. Kindly add below details and submit the designs- Company name- Fernholt Engineering Contracts LLP Name & Post- Varun Kelkar (Designated Partner) Address- Block No.712, Wing C, Tulsa Trade Court, Moti Lal Road, Pawar Industrial Estate, Goregaon(E), Mumbai - 400 063 Contact- +91 97410 58263 Email- varunkelkar@mailnest.example Website- www.fernholtcontracts.example Contact for Letterhead- +91-22-27481195

Hi Tanvir Haque, We are liking your Design #41927306. We have suggested some changes which are mentioned in feedback. Kindly revert with it asap to finalize this design.

Colors

Designer to choose colors to be used in the design.

```html
<!DOCTYPE html>
<html lang="en">
<head>
<meta charset="utf-8">
<title>Fernholt Contracts – Business Card</title>
<link href="https://fonts.googleapis.com/css2?family=Arimo:wght@400;700&display=swap" rel="stylesheet">
<style>
  :root {
    --backdrop: #e9e9e9;
    --card-dark: #2f2f31;
    --card-deep: #272729;
    --panel-tone: #39393b;
    --band-white: #ffffff;
    --ink-dark: #2a2a2a;
    --ink-light: #f2f2f2;
    --ink-muted: #d6d6d6;
  }
  * { margin: 0; padding: 0; box-sizing: border-box; }
  html, body {
    width: 1200px; height: 802px; overflow: hidden;
    background: var(--backdrop);
    font-family: "Arimo", Arial, sans-serif;
  }
  .stage {
    position: relative; width: 1200px; height: 802px;
    display: flex; align-items: center; justify-content: center; gap: 40px;
  }
  .card {
    position: relative; width: 540px; height: 309px;
    background: var(--card-dark);
    box-shadow: 0 6px 18px rgba(0,0,0,.25);
    overflow: hidden;
  }
  /* Front */
  .front .white-band {
    position: absolute; left: 0; right: 0; top: 26px; height: 64px;
    background: var(--band-white);
  }
  .front .person { position: absolute; left: 34px; top: 40px; color: var(--ink-dark); }
  .front .person-name { font-weight: 700; font-size: 17px; letter-spacing: .5px; }
  .front .person-role { font-size: 13px; margin-top: 3px; }
  .front .brand-square {
    position: absolute; right: 22px; top: 26px;
    width: 64px; height: 64px; background: var(--band-white);
    border: 6px solid var(--card-dark);
  }
  .front .brand-name {
    position: absolute; right: 22px; top: 98px; text-align: right;
    color: var(--ink-light); font-weight: 700; font-size: 15px;
    letter-spacing: 1px; line-height: 1.2; white-space: nowrap;
  }
  .front .address {
    position: absolute; right: 22px; top: 152px; text-align: right;
    font-style: normal;
    color: var(--ink-muted); font-size: 12.5px; line-height: 1.45;
  }
  .front .contacts {
    position: absolute; left: 30px; bottom: 20px; list-style: none;
    color: var(--ink-muted); font-size: 12.5px; line-height: 1.6;
  }
  .front .contacts li { display: flex; align-items: center; gap: 7px; }
  .front .contacts svg { width: 11px; height: 11px; flex: none; }
  /* Back */
  .back { background: var(--card-deep); }
  .back .panel {
    position: absolute; right: 0; top: 0; bottom: 0; width: 290px;
    background: var(--panel-tone);
  }
  .back .mark-area {
    position: absolute; left: 40px; top: 40px; width: 200px; height: 229px;
    background: linear-gradient(135deg, #333335, #444446);
  }
  .back .brand-name {
    position: absolute; right: 26px; bottom: 44px; text-align: right;
    color: var(--ink-light); font-weight: 700; font-size: 17px;
    letter-spacing: 1px; line-height: 1.25;
  }
</style>
</head>
<body>
<main class="stage">
  <section class="card front">
    <div class="white-band"></div>
    <div class="person">
      <div class="person-name">VARUN KELKAR</div>
      <div class="person-role">Designated Partner</div>
    </div>
    <div class="brand-square"></div>
    <div class="brand-name">FERNHOLT<br>CONTRACTS</div>
    <address class="address">
      Block No.712, Wing C<br>
      Tulsa Trade Court, Moti Lal Road<br>
      Pawar Industrial Estate<br>
      Goregaon(E), Mumbai - 400 063
    </address>
    <ul class="contacts">
      <li><svg viewBox="0 0 12 12"><circle cx="6" cy="6" r="6" fill="#d6d6d6"/><path d="M4 3.2l1 1.6-.6.6c.4.9 1.1 1.6 2 2l.6-.6 1.6 1-.6 1.1C5.6 8.8 3.2 6.4 3 4z" fill="#2f2f31"/></svg>+91 97410 58263</li>
      <li><svg viewBox="0 0 12 12"><rect x="0.5" y="2" width="11" height="8" fill="#d6d6d6"/><path d="M1 2.5l5 4 5-4" stroke="#2f2f31" fill="none"/></svg>varunkelkar@mailnest.example</li>
      <li><svg viewBox="0 0 12 12"><circle cx="6" cy="6" r="5.5" fill="#d6d6d6"/><g stroke="#2f2f31" fill="none" stroke-width=".8"><ellipse cx="6" cy="6" rx="2.2" ry="5"/><path d="M1 6h10"/></g></svg>www.fernholtcontracts.example</li>
    </ul>
  </section>

  <section class="card back">
    <div class="panel"></div>
    <div class="mark-area" role="img" aria-label="Large embossed brand mark area"></div>
    <div class="brand-name">FERNHOLT<br>CONTRACTS</div>
  </section>
</main>
</body>
</html>
```